Essential Oil 15ml - package of 6

Design of a box of 6 different essential oils.
+ design of the bottle stickers
My bottles are 15ml clear blue glass.

The pictures attached are my competitors...

Target Market(s)

BRAMBLEWICK USA

Font styles to use
Serif

Requirements
Must have
• Our logo + "essential oil" and type (lavender, eucalyptus etc....)
• 15ml - 0.50 fl.oz.
• special color for the oil type.

```html
<!DOCTYPE html>
<html lang="en">
<head>
<meta charset="utf-8">
<title>Sela Springs Essential Oils – Bottle Labels</title>
<link rel="stylesheet" href="https://fonts.googleapis.com/css2?family=Crimson+Text:wght@600&family=Open+Sans:wght@300;400;600&display=swap">
<style>
  :root {
    --canvas-bg: #fdf9fa;
    --label-paper: #f1f1f0;
    --label-ink: #2b2b2b;
    --eucalyptus-band: #29a4c6;
    --eucalyptus-base: #147f98;
    --lavanda-band: #a5679f;
    --lavanda-base: #7b3b7c;
    --peppermint-band: #1f9d4b;
    --peppermint-base: #0f793a;
    --orange-band: #d99c3e;
    --orange-base: #b97b1f;
  }
  * { box-sizing: border-box; margin: 0; padding: 0; }
  html, body { width: 1200px; height: 646px; overflow: hidden; }
  body { background: var(--canvas-bg); position: relative; }
  .label-set {
    position: absolute;
    top: 307px;
    left: 288px;
    display: flex;
    gap: 46px;
  }
  .label {
    width: 122px;
    height: 151px;
    display: flex;
    flex-direction: column;
    box-shadow: 0 4px 12px rgba(0,0,0,0.08);
  }
  .label__brand {
    height: 75px;
    background: var(--label-paper);
    display: flex;
    flex-direction: column;
    align-items: center;
    justify-content: center;
    gap: 6px;
    padding-top: 2px;
  }
  .brand-dot {
    width: 26px;
    height: 26px;
    border-radius: 50%;
    background: var(--label-ink);
  }
  .brand-name {
    font-family: "Crimson Text", serif;
    font-weight: 600;
    font-size: 16px;
    color: var(--label-ink);
    line-height: 1;
    white-space: nowrap;
  }
  .label__type {
    height: 22px;
    display: flex;
    align-items: center;
    justify-content: center;
    font-family: "Open Sans", sans-serif;
    font-weight: 400;
    font-size: 14px;
    color: #ffffff;
    white-space: nowrap;
  }
  .label__details {
    flex: 1;
    display: flex;
    flex-direction: column;
    align-items: center;
    padding-top: 5px;
    font-family: "Open Sans", sans-serif;
  }
  .purity-badge {
    border: 1px solid rgba(20,20,20,0.8);
    padding: 0 6px;
    font-size: 7.5px;
    font-weight: 600;
    color: #1c1c1c;
    line-height: 1.3;
  }
  .product-kind {
    margin-top: 3px;
    font-size: 12.5px;
    font-weight: 300;
    color: rgba(255,255,255,0.38);
    line-height: 1.2;
  }
  .volume {
    margin-top: 2px;
    font-size: 5.5px;
    color: rgba(255,255,255,0.75);
  }
  .label--eucalyptus .label__type { background: var(--eucalyptus-band); }
  .label--eucalyptus .label__details { background: var(--eucalyptus-base); }
  .label--lavanda .label__type { background: var(--lavanda-band); }
  .label--lavanda .label__details { background: var(--lavanda-base); }
  .label--peppermint .label__type { background: var(--peppermint-band); }
  .label--peppermint .label__details { background: var(--peppermint-base); }
  .label--orange .label__type { background: var(--orange-band); }
  .label--orange .label__details { background: var(--orange-base); }
</style>
</head>
<body>
  <main class="label-set">
    <article class="label label--eucalyptus">
      <div class="label__brand"><span class="brand-dot"></span><span class="brand-name">Sela Springs</span></div>
      <div class="label__type">EUCALYPTUS</div>
      <div class="label__details">
        <span class="purity-badge">100% Pure</span>
        <span class="product-kind">Essential Oils</span>
        <span class="volume">0.5 fl. Oz (15ml)</span>
      </div>
    </article>
    <article class="label label--lavanda">
      <div class="label__brand"><span class="brand-dot"></span><span class="brand-name">Sela Springs</span></div>
      <div class="label__type">LAVANDA</div>
      <div class="label__details">
        <span class="purity-badge">100% Pure</span>
        <span class="product-kind">Essential Oils</span>
        <span class="volume">0.5 fl. Oz (15ml)</span>
      </div>
    </article>
    <article class="label label--peppermint">
      <div class="label__brand"><span class="brand-dot"></span><span class="brand-name">Sela Springs</span></div>
      <div class="label__type">PEPPERMINT</div>
      <div class="label__details">
        <span class="purity-badge">100% Pure</span>
        <span class="product-kind">Essential Oils</span>
        <span class="volume">0.5 fl. Oz (15ml)</span>
      </div>
    </article>
    <article class="label label--orange">
      <div class="label__brand"><span class="brand-dot"></span><span class="brand-name">Sela Springs</span></div>
      <div class="label__type">ORANGE</div>
      <div class="label__details">
        <span class="purity-badge">100% Pure</span>
        <span class="product-kind">Essential Oils</span>
        <span class="volume">0.5 fl. Oz (15ml)</span>
      </div>
    </article>
  </main>
</body>
</html>
```